Luxury Bath Flyer

I would like to have a professional Flyer, which would describe a beautiful atmospheric luxury-Bath situation. I am sending you a( screenshot) Flyer Proposal, which shoes my intention and wish how I would like to have it. Please note that Ästhetik and a professional Flyer is very important to me. If possible send a psd.file or a indesign file, in case of we gonna need to change the text. You are also free to make 2 different proposals and one as you would suggest.?(I send you couple pictures, but the main one which I choose on the pdf file, please keep that, it is called " KR-71" - If there is a question please let me know. Looking forward to receive an amazing artwork.Kind Regards Merle
Look and feel
Each slider illustrates characteristics of the customer's brand and the style your logo design should communicate.

```html
<!DOCTYPE html>
<html lang="de">
<head>
<meta charset="utf-8">
<title>Wohnquelle – Bad zum Fixpreis</title>
<link href="https://fonts.googleapis.com/css2?family=Montserrat:wght@400;500;600;700;800&display=swap" rel="stylesheet">
<style>
  :root{
    --blue:#1670b8;
    --blue-dark:#0d5fa3;
    --black:#151515;
    --orange:#ec6a22;
    --orange-pale:#f3c7ad;
    --sand:#b8aa98;
    --panel:#e8e5df;
    --ink:#1d1d1d;
    --white:#ffffff;
    --page:#e9ebee;
  }
  *{box-sizing:border-box;margin:0;padding:0}
  html,body{width:1200px;height:1200px;overflow:hidden;background:var(--page);font-family:'Montserrat',sans-serif}
  .flyer{position:absolute;left:242px;top:91px;width:716px;height:1018px;background:var(--white);overflow:hidden}
  .hero-photo{position:absolute;left:0;top:102px;width:716px;height:428px;
    background:linear-gradient(160deg,#dcd6ce 0%,#cfc6bb 40%,#9c8a76 75%,#6e5a47 100%)}
  .header-shapes{position:absolute;left:0;top:0;width:716px;height:150px}
  .web{position:absolute;left:28px;top:12px;color:var(--white);font-weight:700;font-size:21px;letter-spacing:.3px}
  .social{position:absolute;left:25px;top:47px;display:flex;gap:8px}
  .social span{width:28px;height:28px;border-radius:50%;border:2px solid var(--white);background:rgba(255,255,255,.15)}
  .brand-badge{position:absolute;left:528px;top:20px;width:140px;height:140px;border-radius:50%;
    background:var(--white);border:6px solid var(--orange);display:flex;align-items:center;justify-content:center}
  .brand-name{font-weight:800;font-size:19px;color:var(--black)}
  .tagline{position:absolute;left:0;top:530px;width:716px;height:107px;background:var(--sand);color:var(--white)}
  .tagline p{position:absolute;white-space:nowrap;font-size:21px;font-weight:500;letter-spacing:.3px}
  .tagline .lead{left:34px;top:13px;font-weight:700;font-size:21.5px}
  .tagline .l2{left:100px;top:42px}
  .tagline .l3{left:146px;top:71px}
  .card{position:absolute;top:658px;height:268px;background:var(--panel)}
  .card.services{left:28px;width:319px}
  .card.benefits{left:371px;width:318px}
  .card-title{position:absolute;top:16px;height:36px;color:var(--white);font-weight:700;font-size:21px;letter-spacing:.6px;line-height:36px}
  .services .card-title{left:-28px;width:347px;padding-left:31px;background:linear-gradient(90deg,var(--orange) 0%,var(--orange) 40%,var(--orange-pale) 100%)}
  .benefits .card-title{left:0;width:345px;padding-right:28px;text-align:right;background:linear-gradient(90deg,var(--orange-pale) 0%,var(--orange) 60%,var(--orange) 100%)}
  .card ul{position:absolute;top:86px;list-style:none;font-size:19px;line-height:24.6px;color:var(--ink);font-weight:500}
  .services ul{left:30px;width:285px}
  .benefits ul{left:24px;width:290px}
  .card li{position:relative;padding-left:18px}
  .services li::before{content:"";position:absolute;left:0;top:10px;width:8px;height:8px;border-radius:50%;background:var(--blue)}
  .services li.alt::before{background:var(--orange)}
  .benefits li{padding-left:22px}
  .benefits li svg{position:absolute;left:0;top:5px}
  .footer{position:absolute;left:0;top:944px;width:716px;height:74px;background:var(--orange);color:var(--white)}
  .contact{position:absolute;left:32px;font-size:17.5px;font-weight:500;display:flex;align-items:center;gap:9px;white-space:nowrap}
  .contact.mail{top:14px}
  .contact.addr{top:38px}
  .phone{position:absolute;left:451px;top:18px;width:280px;height:40px;background:var(--white);border-radius:20px 0 0 20px;
    display:flex;align-items:center;gap:10px;padding-left:16px;color:var(--black);font-weight:700;font-size:26px;letter-spacing:.5px}
</style>
</head>
<body>
<main class="flyer">
  <div class="hero-photo" role="img" aria-label="Photo of a modern luxury bathroom with wooden vanity, mosaic wall, tall cabinet and freestanding bathtub"></div>

  <svg class="header-shapes" viewBox="0 0 716 150" aria-hidden="true">
    <polygon points="0,0 716,0 716,102 0,102" fill="var(--black)"/>
    <polygon points="0,0 564,0 0,144" fill="var(--blue)"/>
  </svg>
  <div class="web">www.wohnquelle.at</div>
  <div class="social" aria-label="Social media"><span></span><span></span><span></span><span></span><span></span></div>

  <div class="brand-badge"><span class="brand-name">Wohnquelle</span></div>

  <section class="tagline">
    <p class="lead">Ihr exklusives Bad zum Fixpreis!</p>
    <p class="l2">Wir montieren für Sie...</p>
    <p class="l3">und das „Alles aus einer Hand“!</p>
  </section>

  <section class="card services">
    <h2 class="card-title">UNSERE SERVICES</h2>
    <ul>
      <li>Markenbäder zum Online Preis</li>
      <li class="alt">Wir montieren für Sie</li>
      <li>Funktionalität und Ästhetik</li>
      <li class="alt">Komplettlösungen mit rasche Umsetzung</li>
    </ul>
  </section>

  <section class="card benefits">
    <h2 class="card-title">IHRE VORTEILE</h2>
    <ul>
      <li><svg width="15" height="13" viewBox="0 0 15 13"><path d="M1 7l4 4 9-10" fill="none" stroke="var(--orange)" stroke-width="2"/></svg>Individuelle Badplanung</li>
      <li><svg width="15" height="13" viewBox="0 0 15 13"><path d="M1 7l4 4 9-10" fill="none" stroke="var(--orange)" stroke-width="2"/></svg>Eigene Handwerker vor Ort</li>
      <li><svg width="15" height="13" viewBox="0 0 15 13"><path d="M1 7l4 4 9-10" fill="none" stroke="var(--orange)" stroke-width="2"/></svg>Traumbad erlebniss</li>
    </ul>
  </section>

  <footer class="footer">
    <div class="contact mail">
      <svg width="20" height="14" viewBox="0 0 20 14"><rect x="1" y="1" width="18" height="12" fill="none" stroke="var(--white)" stroke-width="1.6"/><path d="M1 1l9 7 9-7" fill="none" stroke="var(--white)" stroke-width="1.6"/></svg>
      office@wohnquelle.at
    </div>
    <div class="contact addr">
      <svg width="20" height="22" viewBox="0 0 20 22"><path d="M10 1a7 7 0 0 0-7 7c0 5 7 13 7 13s7-8 7-13a7 7 0 0 0-7-7z" fill="var(--white)"/><circle cx="10" cy="8" r="2.6" fill="var(--orange)"/></svg>
      Lindenweg 14, 2391 Talheim am See
    </div>
    <div class="phone">
      <svg width="30" height="30" viewBox="0 0 30 30"><circle cx="15" cy="15" r="13" fill="none" stroke="var(--orange)" stroke-width="2"/><path d="M10 9c1-1 2-1 2.5 0l1.3 2.4c.4.7 0 1.3-.6 1.8-.5.4-.4 1 .1 1.8 1 1.5 2 2.5 3.3 3.2.7.4 1.2.3 1.6-.2.5-.6 1.1-1 1.8-.6l2.3 1.3c.9.5.8 1.6-.1 2.5-1.4 1.4-3.6 1.5-6.3-.4-2.8-2-5-4.8-6.3-7.8-.7-1.8-.6-3 .4-4z" fill="var(--orange)"/></svg>
      0800 417 903
    </div>
  </footer>
</main>
</body>
</html>
```